computter lessons

new business venture [ self employed ] will register my business name as " KEYVORLAN "
what I will offer is :-
computer lessons for new beginners.
Initial set up and basic overview.
lessons per hour in the comfort of your own home.
special rates for customers aged 50+
First lesson is half price with no obligation for booking any further appointments.
a learning and training plan will be presented based on your requirements.
an appraisal update on your new skills.

contact info:-
0161 4970213
07700 900482
larkden@mervoxmail.com

```html
<!DOCTYPE html>
<html lang="en">
<head>
<meta charset="utf-8">
<title>KEYVORLAN – Computer Tuition</title>
<link rel="stylesheet" href="https://fonts.googleapis.com/css2?family=Dancing+Script:wght@500;700&family=Caveat:wght@400&family=Oswald:wght@300&family=Questrial&display=swap">
<style>
  :root {
    --ink: #111111;
    --brand-blue: #1f3fc9;
    --sky-blue: #5aa9f0;
    --cyan-light: #8fe6f7;
    --mid-blue: #2f6cf0;
    --deep-blue: #0b1fd6;
    --paper: #ffffff;
    --white: #ffffff;
  }
  html, body {
    margin: 0;
    padding: 0;
    overflow: hidden;
    background: var(--paper);
  }
  p, h1, ul { margin: 0; padding: 0; }
  .flyer {
    position: relative;
    width: 1200px;
    height: 850px;
    overflow: hidden;
    background: var(--paper);
  }
  .backdrop {
    position: absolute;
    left: 0;
    top: 370px;
    width: 1200px;
    height: 480px;
    background: linear-gradient(180deg,
      rgba(143,230,247,0) 0%,
      rgba(143,230,247,0.55) 18%,
      var(--cyan-light) 32%,
      var(--sky-blue) 50%,
      var(--mid-blue) 68%,
      var(--deep-blue) 100%);
  }
  .brand {
    position: absolute;
    left: 200px;
    top: 55px;
    display: flex;
    align-items: center;
    gap: 30px;
  }
  .brand-mark {
    width: 120px;
    height: 120px;
    background: var(--brand-blue);
  }
  .brand-name {
    font-family: "Dancing Script", cursive;
    font-weight: 700;
    font-size: 90px;
    line-height: 1;
    color: var(--ink);
    letter-spacing: 1px;
  }
  .headline {
    position: absolute;
    left: 0;
    width: 1230px;
    top: 250px;
    text-align: center;
    font-family: "Caveat", cursive;
    font-weight: 400;
    font-size: 76px;
    line-height: 1;
    color: var(--sky-blue);
  }
  .divider {
    position: absolute;
    left: 95px;
    top: 328px;
    width: 1010px;
    height: 1px;
    background: #e6eef8;
  }
  .services {
    position: absolute;
    left: 0;
    top: 350px;
    width: 1160px;
    list-style: none;
    text-align: center;
    font-family: "Dancing Script", cursive;
    font-weight: 500;
    font-size: 40px;
    color: var(--ink);
  }
  .service-row {
    display: block;
    height: 63px;
    line-height: 54px;
  }
  .service {
    display: inline-block;
    margin: 0 10px;
  }
  .service::before {
    content: "";
    display: inline-block;
    width: 15px;
    height: 15px;
    border-radius: 50%;
    background: var(--brand-blue);
    margin-right: 14px;
    vertical-align: middle;
  }
  .offer {
    position: absolute;
    left: 0;
    width: 1160px;
    top: 586px;
    text-align: center;
    font-family: "Oswald", sans-serif;
    font-weight: 300;
    font-size: 34px;
    line-height: 1.2;
    color: var(--white);
  }
  .phones {
    position: absolute;
    left: 0;
    width: 1166px;
    top: 696px;
    text-align: center;
    font-family: "Oswald", sans-serif;
    font-weight: 300;
    font-size: 54px;
    line-height: 1.1;
    letter-spacing: 2px;
    word-spacing: 30px;
    color: var(--white);
  }
  .email {
    position: absolute;
    left: 0;
    width: 1170px;
    top: 762px;
    text-align: center;
    font-family: "Questrial", sans-serif;
    font-size: 60px;
    line-height: 1.1;
    color: var(--white);
  }
</style>
</head>
<body>
  <main class="flyer">
    <div class="backdrop" role="img" aria-label="Geometric pattern of blue and cyan triangles fading in from white"></div>

    <header class="brand">
      <div class="brand-mark"></div>
      <div class="brand-name">KEYVORLAN</div>
    </header>

    <h1 class="headline">Offering Computer Tutition</h1>
    <div class="divider"></div>

    <ul class="services">
      <li class="service-row"><span class="service">Beginner lessons</span><span class="service">Setup and Overview</span><span class="service">In your own home</span></li>
      <li class="service-row"><span class="service">Customised training plans</span><span class="service">Skill Appraisells</span></li>
      <li class="service-row"><span class="service">Special rates for customers aged 50+</span></li>
    </ul>

    <p class="offer">1st Lesson Half Price and Obligation Free</p>

    <p class="phones">07700900482 01614970213</p>
    <p class="email">larkden@mervoxmail.com</p>
  </main>
</body>
</html>
```